Harbor Nine Builders, Inc Biz Cards

Harbor Nine Builders, Inc is a turnkey building solution provider in the Greater Philadelphia Area. We work collaboratively with clients to provide turnkey building services in both the residential and commercial markets.
We are targeting the higher end clients in the commercial market. We have been successful in getting a few commercial projects in , but still rely on our residential work for a large portion of our revenue. We are trying to move almost exclusively toward the commercial market.
Services include;
-Commercial New Construction and Interior Tenant Fit-Outs
-Residential New Construction and Renovations
-Project Management and Owner's Representative Services
Target Market(s)
Tenants in large commerical buildings, higher end home owners, someone with a known budget and dream but unsure how to make it a building reality
Industry/Entity Type
Residential
Contact Information for Business Card
Harbor Nine Builders, Inc.
742 Maple Crescent
Jeffersonville, PA 19403
There are three people that we need to order business cards for.
Dylan Harte
Cell# 484-555-0137
Dylan@Harbor-Nine-Builders.example
Marco Fellingham
Cell# 610-555-0192
Marco@Harbor-Nine-Builders.example
Ray Holt
Cell# 267-555-0148
Ray@Harbor-Nine-Builders.example
HIC#PA579024
www.harbor-nine-builders.example (under construction)
We like our written our logo Harbor Nine Builders, Inc with red, blue, and grey. We do not like the Harbor Nine Builders, Inc. with spinning arrows as, however like the incorporation of the spinning around arrows to represent "turnkey" building services.

```html
<!DOCTYPE html>
<html lang="en">
<head>
<meta charset="utf-8">
<title>Harbor Nine Builders, Inc. – Business Card</title>
<link rel="stylesheet" href="https://fonts.googleapis.com/css2?family=Michroma&family=Roboto:wght@400&display=swap">
<style>
  :root {
    --page-bg: #e9e9ea;
    --card-white: #ffffff;
    --card-shade: #eef0f2;
    --blue-light: #1f84d6;
    --blue-mid: #1560b4;
    --blue-deep: #0c3f8c;
    --brand-blue: #1d4fa0;
    --ink-dark: #2c2f36;
    --ink-grey: #6d7178;
    --on-blue: #ffffff;
  }
  html, body {
    margin: 0;
    width: 1200px;
    height: 1085px;
    overflow: hidden;
    background: var(--page-bg);
  }
  .canvas {
    position: relative;
    width: 1200px;
    height: 1085px;
  }
  .business-card {
    position: absolute;
    left: 100px;
    top: 257px;
    width: 1000px;
    height: 570px;
    background: linear-gradient(120deg, var(--card-white) 55%, var(--card-shade) 100%);
    box-shadow: 0 18px 40px rgba(0, 0, 0, 0.18);
    overflow: hidden;
  }
  .contact-panel {
    position: absolute;
    left: 0;
    top: 0;
    width: 1000px;
    height: 570px;
  }
  .contact-group {
    position: absolute;
    right: 600px;
    text-align: right;
    font-family: "Michroma", "Arial", sans-serif;
    font-size: 15px;
    line-height: 30px;
    color: var(--on-blue);
    white-space: nowrap;
  }
  .contact-group--phone { top: 100px; }
  .contact-group--address { top: 236px; }
  .contact-group--web { top: 400px; }
  .brand-block {
    position: absolute;
    left: 566px;
    top: 112px;
    width: 400px;
  }
  .brand-name {
    margin: 0;
    font-family: "Michroma", "Arial", sans-serif;
    font-size: 31px;
    line-height: 46px;
    color: var(--brand-blue);
  }
  .brand-tagline {
    margin: 14px 0 0;
    font-family: "Roboto", "Arial", sans-serif;
    font-size: 14px;
    color: var(--ink-grey);
    letter-spacing: 0.3px;
  }
  .holder {
    position: absolute;
    left: 566px;
    top: 380px;
  }
  .holder-name {
    margin: 0;
    font-family: "Michroma", "Arial", sans-serif;
    font-size: 28px;
    color: var(--brand-blue);
    letter-spacing: 1px;
  }
  .holder-role {
    margin: 8px 0 0;
    font-family: "Michroma", "Arial", sans-serif;
    font-size: 19px;
    color: var(--ink-dark);
  }
</style>
</head>
<body>
<main class="canvas">
  <section class="business-card">
    <svg class="contact-panel" width="1000" height="570" viewBox="0 0 1000 570" aria-hidden="true">
      <defs>
        <radialGradient id="panel-blue" cx="0.45" cy="0.5" r="0.75">
          <stop offset="0" stop-color="#1f84d6"/>
          <stop offset="0.55" stop-color="#1560b4"/>
          <stop offset="1" stop-color="#0c3f8c"/>
        </radialGradient>
      </defs>
      <path fill="url(#panel-blue)" d="M0 0 H430 C470 0 492 80 488 130 C485 175 445 170 445 205 C445 240 488 235 488 280 C488 325 445 320 445 355 C445 390 488 385 488 430 C490 490 470 570 430 570 H0 Z"/>
      <g fill="none" stroke="#ffffff" stroke-width="2.5">
        <circle cx="440" cy="130" r="22"/>
        <path d="M432 120 q-3 3 0 9 q5 9 14 14 q6 3 9 0 l-4 -5 q-3 2 -5 0 q-5 -4 -8 -8 q-2 -2 0 -5 z" fill="#ffffff" stroke="none"/>
        <circle cx="440" cy="280" r="22"/>
        <path d="M440 294 C433 285 430 280 430 275 a10 10 0 0 1 20 0 c0 5 -3 10 -10 19 z" fill="#ffffff" stroke="none"/>
        <circle cx="440" cy="275" r="3.5" fill="#1560b4" stroke="none"/>
        <circle cx="440" cy="430" r="22"/>
        <circle cx="440" cy="430" r="12" stroke-width="2"/>
        <ellipse cx="440" cy="430" rx="5" ry="12" stroke-width="1.6"/>
        <line x1="428" y1="430" x2="452" y2="430" stroke-width="1.6"/>
        <line x1="431" y1="423" x2="449" y2="423" stroke-width="1.4"/>
        <line x1="431" y1="437" x2="449" y2="437" stroke-width="1.4"/>
      </g>
    </svg>

    <div class="contact-group contact-group--phone">
      <div>Cell# 484-555-0137</div>
      <div>HIC#PA579024</div>
    </div>
    <div class="contact-group contact-group--address">
      <div>742 Maple Crescent,</div>
      <div>Jeffersonville,</div>
      <div>PA 19403</div>
    </div>
    <div class="contact-group contact-group--web">
      <div>Dylan@Harbor-Nine-Builders.example</div>
      <div>www.harbor-nine-builders.example</div>
    </div>

    <div class="brand-block">
      <p class="brand-name">Harbor Nine<br>Builders, Inc.</p>
      <p class="brand-tagline">Innovative Design. Superior Craftsmanship.</p>
    </div>

    <div class="holder">
      <p class="holder-name">DYLAN HARTE</p>
      <p class="holder-role">Managing Director</p>
    </div>
  </section>
</main>
</body>
</html>
```